BHP Business Cards

I need business cards for "copper glen partners llc" doublesided... logo on the back (also include logo on front)
logo attached to project... i have jpg up.. let me know if you need eps file.
Company Info:
842 East Marlow Avenue, Suite 7B
Chicago, Illinois 60617
facsimile 312-555-4186 (list fax, address, website on all cards.)
www.copperglenpartnersllc.example
Three different people on cards:
Dorian K. Patel, CPA MST
Principal
ofc 312-555-0271
mobile 312-555-0388
doriankpatel@copperglenpartnersllc.example
Harold J. Quenby, CPA MST
Principal
haroldjquenby@copperglenpartnersllc.example
mobile 708-555-0149
ofc 312-555-0271
Miles T Carver
Principal
ofc 312-555-0271
no mobile
milestcarver@copperglenpartnersllc.example
I have multiple projects listed.. see below:
Business cards for copper glen partners llc
letterhead
envelopes
Business cards for KM Holdings LLC
letterhead
envelopes
rich people
Business

```html
<!DOCTYPE html>
<html lang="en">
<head>
<meta charset="utf-8">
<title>Copper Glen Partners LLC – Business Card</title>
<link rel="stylesheet" href="https://fonts.googleapis.com/css2?family=Cinzel:wght@500&family=Crimson+Text:wght@400&display=swap">
<style>
  :root {
    --navy: #033f70;
    --backdrop: #c4c4c2;
    --paper: #f2f2f2;
    --rule: #5a6470;
    --charcoal: #3b3b3b;
  }
  * { margin: 0; padding: 0; box-sizing: border-box; }
  html, body { width: 1200px; height: 453px; overflow: hidden; background: var(--backdrop); }
  .stage { position: relative; width: 1200px; height: 453px; }

  .card {
    position: absolute; top: 38px; width: 560px; height: 370px;
    background: var(--paper);
    box-shadow: 4px 5px 6px rgba(0,0,0,.45);
    overflow: hidden;
  }
  .card--front { left: 32px; }
  .card--back { left: 614px; }

  .front-band { position: absolute; left: 0; width: 100%; background: var(--navy); }
  .front-band--top { top: 0; height: 97px; }
  .front-band--bottom { top: 278px; height: 92px; }

  .brand-name {
    position: absolute; left: 0; width: 100%;
    text-align: center; color: var(--navy);
    font-family: "Cinzel", serif; font-weight: 500;
    white-space: nowrap;
  }
  .card--front .brand-name { top: 170px; font-size: 24px; letter-spacing: 1px; }

  .back-art { position: absolute; inset: 0; }

  .card--back .brand-name { left: 10px; width: 200px; top: 217px; font-size: 10px; letter-spacing: .2px; }

  .holder {
    position: absolute; right: 6px; top: 22px; text-align: right; color: #fff;
    font-family: "Crimson Text", serif;
  }
  .holder-name { font-size: 15px; letter-spacing: .6px; line-height: 18px; text-transform: uppercase; }
  .holder-title { font-size: 13px; letter-spacing: 3.2px; line-height: 16px; margin-top: 8px; }

  .contact {
    position: absolute; color: var(--navy);
    font-family: "Crimson Text", serif; font-size: 13.5px; white-space: nowrap;
  }
  .contact--phone { left: 316px; top: 138px; }
  .contact--email { left: 288px; top: 189px; font-size: 13px; }
  .contact--web { left: 262px; top: 237px; }
  .contact--address { left: 234px; top: 289px; font-size: 13px; }
</style>
</head>
<body>
<div class="stage">

  <section class="card card--front">
    <div class="front-band front-band--top"></div>
    <div class="front-band front-band--bottom"></div>
    <div class="brand-name">Copper Glen Partners LLC</div>
  </section>

  <section class="card card--back">
    <svg class="back-art" width="560" height="370" viewBox="0 0 560 370" aria-hidden="true">
      <defs>
        <linearGradient id="sheen" x1="0" y1="0" x2="1" y2="0.3">
          <stop offset="0" stop-color="#f7f8f9"/>
          <stop offset="0.55" stop-color="#e4e9ee"/>
          <stop offset="1" stop-color="#bccad7"/>
        </linearGradient>
      </defs>
      <polygon points="0,0 322,0 146,370 0,370" fill="url(#sheen)"/>
      <polygon points="322,0 330,0 154,370 146,370" fill="#f7f7f7"/>

      <polygon points="321,16 560,16 560,67 297,67" fill="var(--navy)"/>
      <line x1="454" y1="44" x2="556" y2="44" stroke="#fff" stroke-width="1"/>

      <polygon points="265,137 307,137 297,165 254,165" fill="var(--navy)"/>
      <line x1="297" y1="165.5" x2="560" y2="165.5" stroke="var(--rule)" stroke-width="1"/>
      <circle cx="281" cy="151" r="8.5" fill="none" stroke="#fff" stroke-width="1.6"/>
      <path d="M277.5 146.5c1-.6 1.6 0 2 1l.6 1.2c.2.6-.5 1-.8 1.4.6 1.4 1.4 2.4 2.6 3.2.4-.3.9-1 1.5-.7l1.2.7c.8.5 1 1.1.3 1.8-1 1-2.6.9-4.2-.3-1.7-1.3-3-3-3.6-5-.4-1.4-.2-2.6.4-3.3z" fill="#fff"/>

      <polygon points="236,189 278,189 268,217 225,217" fill="var(--navy)"/>
      <line x1="268" y1="217.5" x2="560" y2="217.5" stroke="var(--rule)" stroke-width="1"/>
      <rect x="243" y="197" width="17" height="12" fill="#fff"/>
      <polyline points="243,197 251.5,204 260,197" fill="none" stroke="var(--navy)" stroke-width="1.2"/>

      <polygon points="210,237 252,237 242,265 199,265" fill="var(--navy)"/>
      <line x1="242" y1="265.5" x2="560" y2="265.5" stroke="var(--rule)" stroke-width="1"/>
      <g fill="none" stroke="#fff" stroke-width="1.4">
        <circle cx="226" cy="251" r="8.5"/>
        <ellipse cx="226" cy="251" rx="3.6" ry="8.5"/>
        <line x1="217.5" y1="251" x2="234.5" y2="251"/>
        <line x1="219" y1="246.5" x2="233" y2="246.5"/>
        <line x1="219" y1="255.5" x2="233" y2="255.5"/>
      </g>

      <polygon points="184,289 226,289 216,317 173,317" fill="var(--navy)"/>
      <line x1="216" y1="317.5" x2="560" y2="317.5" stroke="var(--rule)" stroke-width="1"/>
      <path d="M198 295a6 6 0 0 1 6 6c0 4.5-6 11-6 11s-6-6.5-6-11a6 6 0 0 1 6-6z" fill="#fff"/>
      <circle cx="198" cy="301" r="2.2" fill="var(--navy)"/>

      <rect x="0" y="356" width="148" height="14" fill="var(--charcoal)"/>
      <polygon points="160,356 560,356 560,370 153,370" fill="var(--navy)"/>
    </svg>

    <div class="holder">
      <div class="holder-name">Dorian K. Patel, CPA MST</div>
      <div class="holder-title">Principal</div>
    </div>

    <div class="brand-name">Copper Glen Partners LLC</div>

    <div class="contact contact--phone">312-555-0271 , 312-555-0388</div>
    <div class="contact contact--email">doriankpatel@copperglenpartnersllc.example</div>
    <div class="contact contact--web">www.copperglenpartnersllc.example</div>
    <div class="contact contact--address">842 East Marlow Avenue, Suite 7B Chicago, Illinois 60617</div>
  </section>

</div>
</body>
</html>
```